Velora Pedal Journeys Brochure

We need an informational brochure designed to display all of our cycling tours for the 2019 season. The majority of text and images can be pulled from our website - www.velorapedaljourneys.com

We would like to use the colors red (#242424), Grey, and White

```html
<!DOCTYPE html>
<html lang="en">
<head>
<meta charset="utf-8">
<title>Velora Pedal Journeys Brochure</title>
<link href="https://fonts.googleapis.com/css2?family=Oswald:wght@500;700&family=Montserrat:wght@400;500;700&display=swap" rel="stylesheet">
<style>
:root{
  --red:#b5202e;
  --red-dark:#9c1a26;
  --ink:#242424;
  --grey:#8a8a8a;
  --paper:#ffffff;
  --paper-grey:#e9e9e9;
  --stage:#353535;
  --head:'Oswald', 'Arial Narrow', sans-serif;
  --body:'Montserrat', Arial, sans-serif;
}
*{margin:0;padding:0;box-sizing:border-box}
html,body{width:902px;height:1200px;overflow:hidden;background:var(--stage)}
body{position:relative;font-family:var(--body);color:var(--ink)}
.page{position:absolute;overflow:hidden}
.page--light{background:linear-gradient(90deg,#f7f7f7 0%,#ffffff 40%,#e4e4e4 100%)}
.page--light-r{background:linear-gradient(90deg,#d9d9d9 0%,#f4f4f4 12%,#ffffff 60%,#f1f1f1 100%)}
.abs{position:absolute}
.photo{position:absolute}

/* spread 1 left */
.apart-title{font-family:var(--head);font-weight:700;font-size:30px;letter-spacing:.3px;text-align:center;width:100%;top:28px;color:var(--ink)}
.apart-rule{left:160px;top:73px;width:112px;height:2px;background:var(--red)}
.feature{top:90px;width:100px;text-align:center}
.feature h3{font-family:var(--body);font-weight:500;font-size:10px;color:var(--red);margin-bottom:12px;white-space:nowrap;margin-left:-20px;margin-right:-20px}
.feature p{font-size:7.9px;line-height:9.7px;color:var(--ink)}
.contact-band{left:0;top:396px;width:413px;height:84px;background:var(--red)}
.contact-band .seal{left:36px;top:12px;width:60px;height:60px;border:2px solid #fff;border-radius:50%}
.contact-text{left:120px;top:26px;width:196px;text-align:center;color:#fff;font-size:9.4px;line-height:11.6px}
.social{top:29px;width:26px;height:26px;border:1.6px solid #fff;border-radius:50%}
.footer-bar{height:4px;background:var(--ink)}
.folio{height:10px;background:var(--red);color:#fff;font-size:5.5px;font-weight:700;text-align:center;line-height:10px}

/* cover */
.cover-brand{left:30px;top:79px;display:flex;align-items:center;gap:10px;color:#fff}
.cover-brand .ring{width:54px;height:54px;border:2px solid #fff;border-radius:50%}
.cover-brand .name{font-family:var(--body);font-weight:500;font-size:17px;line-height:20px;color:#fff}
.cover-title{left:27px;top:276px;font-family:var(--head);font-weight:700;font-size:35px;line-height:40px;color:#fff;letter-spacing:.2px}
.cover-sub{left:33px;top:355px;font-size:10.4px;line-height:12.5px;color:#fff}
.cover-note{left:0;top:456px;width:100%;text-align:center;font-size:9.6px;line-height:11.6px;color:#fff}
.cover-url{left:0;top:496px;width:100%;height:19px;background:rgba(60,40,35,.55);text-align:center;color:#fff;font-size:9.6px;line-height:19px}

/* story page */
.story-band{left:0;top:0;width:413px;height:176px;background:var(--red);border-bottom:3px solid #9a9a9a}
.story-band .seal{left:25px;top:22px;width:100px;height:100px;border:2.4px solid #fff;border-radius:50%}
.story-band .seal::after{content:"";position:absolute;inset:7px;border:1.4px solid #fff;border-radius:50%}
.story{left:134px;top:22px;width:262px;color:#fff}
.story h2{font-family:var(--body);font-weight:500;font-size:13.5px;margin-bottom:4px}
.story p{font-size:6.3px;line-height:8px;margin-bottom:7px}
.premier{left:0;top:196px;width:100%;text-align:center;font-family:var(--head);font-weight:700;font-size:35px;line-height:41px;color:var(--ink)}
.bike{left:20px;width:130px;height:76px}
.spec{left:164px;width:236px}
.spec h4{font-family:var(--body);font-weight:700;font-size:9px;color:var(--red);margin-bottom:5px}
.spec p{font-size:5.3px;line-height:6.6px;margin-bottom:5px}
.spec ul{list-style:none}
.spec li{font-size:5.3px;line-height:7.4px;padding-left:7px;position:relative}
.spec li::before{content:"";position:absolute;left:0;top:2.2px;width:3px;height:3px;border-radius:50%;background:var(--red)}
.divider{left:39px;top:390px;width:337px;height:1px;background:#9a9a9a}

/* tours */
.tour{position:absolute;width:84px}
.tour .pic{position:relative;width:84px;height:88px;border:2px solid #fff;box-shadow:0 1px 3px rgba(0,0,0,.35)}
.tour .price{position:absolute;left:0;bottom:0;width:100%;height:12px;background:rgba(181,32,46,.92);color:#fff;font-size:6px;font-weight:700;line-height:12px;padding-left:9px}
.tour h5{font-family:var(--head);font-weight:500;font-size:8.8px;line-height:11px;color:var(--red);margin:8px 0 5px;text-transform:uppercase}
.tour .blurb{font-size:5.6px;line-height:7px;padding-bottom:4px;border-bottom:1px dashed #888;margin-bottom:4px}
.tour .facts{font-size:5.6px;line-height:7px}
.callout{left:306px;top:272px;width:94px;text-align:center;font-family:var(--body);font-weight:700;font-size:10px;line-height:12.1px;color:var(--red)}
</style>
</head>
<body>

<!-- Spread 1: left page -->
<section class="page page--light" style="left:38px;top:50px;width:413px;height:534px">
  <h1 class="abs apart-title">WHAT SETS US APART?</h1>
  <div class="abs apart-rule"></div>
  <div class="abs feature" style="left:32px">
    <h3>The Best Routes</h3>
    <p>Our routes have been carefully researched and designed to offer a variety of invigorating and rewarding ride options with a combination of world famous routes, signature Burners, and local secrets.</p>
  </div>
  <div class="abs feature" style="left:157px">
    <h3>Passion Meets Expertise</h3>
    <p>We've combined decades of experience as an industry-leading tour operator, with our passion as cyclists, to create a program that is not only expertly executed, but also fun, challenging, and unique.</p>
  </div>
  <div class="abs feature" style="left:282px">
    <h3>Flexibility</h3>
    <p>With multiple route options preloaded to your Trailmark GPS, there's no pressure to adapt your riding style or pace to the group's. You have the flexibility to make each day the adventure that you want.</p>
  </div>
  <div class="photo" role="img" aria-label="Road cyclist riding toward the camera on a winding road through green hills at sunrise" style="left:0;top:238px;width:413px;height:160px;background:linear-gradient(180deg,#e8eef2 0%,#c9d3c4 30%,#7e9266 55%,#55683f 75%,#8b8a82 100%)"></div>
  <div class="abs contact-band">
    <div class="abs seal"></div>
    <div class="abs contact-text">+1 555 014 2277<br>ride@velorapedaljourneys.com<br>18 Orchard Lane, Millbrook, CA 90000</div>
    <div class="abs social" style="left:331px"></div>
    <div class="abs social" style="left:361px"></div>
  </div>
  <div class="abs footer-bar" style="left:13px;top:518px;width:345px"></div>
  <div class="abs folio" style="left:362px;top:511px;width:22px"></div>
</section>

<!-- Spread 1: cover -->
<section class="page" style="left:451px;top:50px;width:413px;height:534px">
  <div class="photo" role="img" aria-label="Mountain biker riding red desert slickrock beneath a natural stone arch at sunset" style="inset:0;background:linear-gradient(160deg,#a8432a 0%,#c9673f 25%,#9a4a36 50%,#6e3428 75%,#4a2a24 100%)"></div>
  <div class="abs cover-brand"><div class="ring"></div><div class="name">Velora Pedal<br>Journeys</div></div>
  <h2 class="abs cover-title">IT'S ALL ABOUT<br>THE RIDE</h2>
  <p class="abs cover-sub">Cycling and mountain bike adventures that<br>turn your bucket list into a bike-it list</p>
  <p class="abs cover-note">Our Cycling Adventures are designed for active to avid riders and pay<br>homage to the greatest biking routes in North America.<br>For those about to ride, we salute you.</p>
  <div class="abs cover-url">www.velorapedaljourneys.com</div>
</section>

<!-- Spread 2: story page -->
<section class="page page--light" style="left:38px;top:616px;width:413px;height:534px">
  <div class="abs story-band">
    <div class="abs seal"></div>
    <div class="abs story">
      <h2>Our Story</h2>
      <p>Velora Pedal Journeys was born from decades of experience as North America's leading specialist tour operator and a lifelong passion for cycling and mountain biking. We wanted to create a series of tours made for bikers by bikers, that highlight not only the most famous rides in the country, but also our favorites.</p>
      <p>While we have some amazing colleagues in the industry, we've found many tours to be slowed down by lazy days and charcuterie. While there's always time for cold, hazy IPA's and bold Cabernets, we find they taste better after cruising some of the most incredible rides of your life. Our mantra, "It's all about the ride," emphasizes our desire to create unique itineraries that will test your abilities, and help you find your strongest flow.</p>
      <p>Velora Pedal Journeys is where passion meets experience.</p>
    </div>
  </div>
  <h2 class="abs premier">A PREMIER CYCLING<br>EXPERIENCE</h2>
  <div class="photo bike" role="img" aria-label="White gravel road bike with red accents, side view" style="top:292px;background:linear-gradient(180deg,#f2f2f2,#d6d6d6)"></div>
  <div class="abs spec" style="top:290px">
    <h4>ROAD</h4>
    <p>When searching for a bike to suit the Velora Pedal Journeys ethos we had to be sure of a few things. For one, it had to perfectly perform regardless of long days on the pavement and detours onto rugged or rocky country roads.</p>
    <p>This search led us to the Ridgeline Wayfarer. Not quite a cross-bike but not completely a road bike either, the Wayfarer is perfect for Velora Pedal Journeys.</p>
    <ul>
      <li>Carbon fiber fork and frame</li>
      <li>Crest elite disc wheels with premier Ridgeline Summit Pro tires</li>
      <li>Hydraulic disc brakes</li>
      <li>11 speed derailleur system</li>
    </ul>
  </div>
  <div class="abs divider"></div>
  <div class="photo bike" role="img" aria-label="Black full-suspension mountain bike, side view" style="top:412px;background:linear-gradient(180deg,#f0f0f0,#d2d2d2)"></div>
  <div class="abs spec" style="top:404px">
    <h4>MOUNTAIN</h4>
    <p>The iconic Ridgeline Switchback Carbon is the definition of a go everywhere, do everything trail bike.</p>
    <p>Voted "The #1 trail bike of 2017" by trailnotes.com, the Switchback balances technical fun with high speed stability, allowing you to tear up tight turns, or flow through major downhills.</p>
    <ul>
      <li>CORE 9m carbon fiber Trail Chassis</li>
      <li>ForkWorks Ascent RC fork</li>
      <li>Quad-link Suspension</li>
      <li>11-speed trail groupset</li>
      <li>Stash Trapdoor</li>
    </ul>
  </div>
  <div class="abs footer-bar" style="left:13px;top:518px;width:345px"></div>
  <div class="abs folio" style="left:362px;top:513px;width:22px">01</div>
</section>

<!-- Spread 2: tours page -->
<section class="page page--light-r" style="left:451px;top:616px;width:413px;height:534px">
  <article class="tour" style="left:19px;top:30px">
    <div class="pic" role="img" aria-label="Vineyard rows below purple hills" style="background:linear-gradient(180deg,#8fb3d6 0%,#c8a98a 45%,#5c6e3a 75%,#3e4a26 100%)"><span class="price">FROM US $2599</span></div>
    <h5>Napa and the Sonoma Coast</h5>
    <p class="blurb">Discover the beautiful rolling hills and rocky coastline of Northern California's legendary wine region.</p>
    <p class="facts">Duration: 6 Days / 5 Nights<br>Departure City: Napa, CA<br>Ends In: Napa, CA<br>Accommodation: 3-4 Star Hotels</p>
  </article>
  <article class="tour" style="left:116px;top:30px">
    <div class="pic" role="img" aria-label="Cyclist under oak trees on a coastal path" style="background:linear-gradient(180deg,#b9c6a4 0%,#6f7b52 45%,#4d5636 75%,#8c8470 100%)"><span class="price">FROM US $2549</span></div>
    <h5>Santa Barbara and the Central Coast</h5>
    <p class="blurb">Escape the concrete jungle with a 6-day tour of California's central coast filled with diverse landscapes and sandy beaches.</p>
    <p class="facts">Duration: 6 Days / 5 Nights<br>Departure City: Los Angeles, CA<br>Ends In: Los Angeles, CA<br>Accommodation: 3-4 Star Hotels</p>
  </article>
  <article class="tour" style="left:214px;top:30px">
    <div class="pic" role="img" aria-label="Road winding through orange autumn forest" style="background:linear-gradient(180deg,#e0a43c 0%,#c46a22 45%,#8a4a20 75%,#6a5a3a 100%)"><span class="price">FROM US $2549</span></div>
    <h5>Vermont's Green Glory</h5>
    <p class="blurb">Whether climbing Smugglers Notch, or cruising along the shoreline of Lake Champlain, Vermont's incredible landscape provides an ideal backdrop for challenging, and beautiful rides.</p>
    <p class="facts">Duration: 6 Days / 5 Nights<br>Departure City: Burlington, VT Ends In: Burlington, VT<br>Accommodation: 3-4 Star Hotels</p>
  </article>
  <article class="tour" style="left:311px;top:30px">
    <div class="pic" role="img" aria-label="Saguaro cactus silhouette against a red sunset sky" style="background:linear-gradient(180deg,#3c2a5a 0%,#b7303a 45%,#e8703a 70%,#3a1e1a 100%)"><span class="price">FROM US $2199</span></div>
    <h5>Saguaros and Cycles</h5>
    <p class="blurb">Ride through the desert on a bike with no name on an incredible circuit through Southern Arizona's Sonoran Desert.</p>
    <p class="facts">Duration: 6 Days / 5 Nights<br>Departure City: Tucson, AZ<br>Ends In: Tucson, AZ<br>Accommodation: 3-4 Star Hotels</p>
  </article>
  <article class="tour" style="left:19px;top:270px">
    <div class="pic" role="img" aria-label="Island lake and mountains with autumn trees" style="background:linear-gradient(180deg,#6f9cc8 0%,#3a6e98 40%,#c79a3e 70%,#6a6a5a 100%)"><span class="price">FROM US $2395</span></div>
    <h5>Bikecouver Island</h5>
    <p class="blurb">Ride the Pacific Marine Circle to discover the ancient forests, rugged mountains, and breathtaking coasts of Vancouver Island.</p>
    <p class="facts">Duration: 6 Days / 5 Nights<br>Departure City: Victoria, BC<br>Ends In: Victoria, BC<br>Accommodation: 3-4 Star Hotels</p>
  </article>
  <article class="tour" style="left:116px;top:270px">
    <div class="pic" role="img" aria-label="Red rock canyon hoodoos under a purple sky" style="background:linear-gradient(180deg,#5a4a9a 0%,#c8507a 35%,#d8603a 65%,#8a3020 100%)"><span class="price">FROM US $2495</span></div>
    <h5>Cycles, Cliffs, and Canyons</h5>
    <p class="blurb">Join us for a ride through the glowing orange, and red rock mazes of Southern Utah's alien landscape.</p>
    <p class="facts">Duration: 6 Days / 5 Nights<br>Departure City: Las Vegas, NV<br>Ends In: Las Vegas, NV<br>Accommodation: 3-4 Star Hotels</p>
  </article>
  <article class="tour" style="left:214px;top:270px">
    <div class="pic" role="img" aria-label="Green valley and mesas under blue sky with clouds" style="background:linear-gradient(180deg,#4a7ab8 0%,#d8e2ea 35%,#6e8a48 65%,#a07a4a 100%)"><span class="price">FROM US $2595</span></div>
    <h5>Pedals and Pueblos</h5>
    <p class="blurb">Explore the land of the ancient Anasazi, and the incredibly diverse landscapes that inspired Elena Marsh's legendary works in the enchanted state of New Mexico.</p>
    <p class="facts">Duration: 6 Days / 5 Nights<br>Departure City: Santa Fe, NM<br>Ends In: Santa Fe, NM<br>Accommodation: 3-4 Star Hotels</p>
  </article>
  <p class="abs callout">Test your skills on our signature Burner routes. These rides will have you burning rubber and calories with extended sections of dirt track, and gravel roads. Depending on the route you choose, you'll probably feel the burn in your legs as well your lungs.</p>
  <div class="abs footer-bar" style="left:13px;top:518px;width:344px"></div>
  <div class="abs folio" style="left:363px;top:513px;width:22px">02</div>
</section>

</body>
</html>
```